MAREK DOLVANE FOR CONGRESS DISTRICT 32

I need to create a campaign flyer for my congress campaign. I am running for congress in District 32 of Texas as a republican. I am a former Olympic athlete, world champion fencer, Army veteran, Counterintelligence officer (I catch spies).
I want just my first name MAREK in big letters at the top. I want it to say MAREK and below it Republican for Congress.
www.marekforcongress.example

Industry/Entity Type

Political

Colors
EB3D1F
EC4F4E
F09395
F8D3D4
FCEDEE

Requirements
Nice to have
• Would love a catchy title for the Flyer like "Spy Catcher", "Olympic Athlete" "World Champion Fencer" running for Congress in your District!

```html
<!DOCTYPE html>
<html lang="en">
<head>
<meta charset="utf-8">
<title>Marek Dolvane for Congress – Flyer</title>
<link rel="stylesheet" href="https://fonts.googleapis.com/css2?family=Josefin+Sans:wght@600;700&family=Montserrat:wght@800&display=swap">
<style>
  :root {
    --navy-deep: #141a4a;
    --navy: #1f2766;
    --navy-bright: #2b3589;
    --red-deep: #6e0812;
    --red: #a3101c;
    --flag-red: #c8001e;
    --white: #ffffff;
    --paper: #f3f3f8;
    --link-blue: #27357a;
    --star-red: #d42a2f;
  }
  * { margin: 0; padding: 0; box-sizing: border-box; }
  html, body { width: 927px; height: 1200px; overflow: hidden; background: var(--navy-deep); }
  .flyer {
    position: relative;
    width: 927px;
    height: 1200px;
    overflow: hidden;
    color: var(--white);
    font-family: "Josefin Sans", "Helvetica Neue", Arial, sans-serif;
  }
  .backdrop {
    position: absolute; inset: 0;
    background:
      radial-gradient(ellipse 420px 300px at 300px 560px, rgba(60,70,170,.45), transparent 70%),
      linear-gradient(160deg, var(--red) 0%, var(--red-deep) 32%, var(--navy) 55%, var(--navy-deep) 100%);
  }
  .backdrop__left {
    position: absolute; inset: 0;
    background: linear-gradient(100deg, #14205a 0%, #1c2a6e 60%, rgba(28,42,110,0) 100%);
    clip-path: polygon(0 0, 290px 0, 0 800px);
  }
  .backdrop__right {
    position: absolute; inset: 0;
    background: linear-gradient(100deg, var(--flag-red) 0%, var(--white) 40%, var(--flag-red) 70%, #9c0018 100%);
    clip-path: polygon(670px 0, 927px 0, 927px 750px);
    opacity: .95;
  }
  .campaign-mark {
    position: absolute;
    left: 338px; top: 446px;
    display: flex; align-items: center; gap: 12px;
    font-family: "Montserrat", Arial, sans-serif;
    font-weight: 800;
    color: var(--white);
  }
  .campaign-mark__name { display: block; font-size: 45px; line-height: 46px; letter-spacing: 0.5px; }
  .campaign-mark__line { display: block; font-size: 21px; line-height: 24px; letter-spacing: 0.2px; }
  .campaign-mark__square { width: 40px; height: 40px; background: var(--white); }
  .headline { position: absolute; left: 157px; top: 560px; width: 613px; height: 270px; }
  .headline text { fill: var(--white); font-family: "Josefin Sans", Arial, sans-serif; font-weight: 700; }
  .info-box { position: absolute; left: 157px; top: 848px; width: 614px; height: 178px; }
  .info-box__web {
    position: absolute; left: 0; top: 0; width: 614px; height: 52px;
  }
  .credentials {
    position: absolute; left: 0; top: 52px; width: 614px; height: 126px;
    display: grid; grid-template-columns: 276px 1fr;
    list-style: none;
  }
  .credentials__col { padding: 24px 0 0 14px; }
  .credentials__col + .credentials__col { padding-left: 16px; }
  .credential {
    display: flex; gap: 8px;
    font-weight: 700; font-size: 21px; line-height: 23px;
    letter-spacing: 1.3px; text-transform: uppercase;
    margin-bottom: 14px;
  }
  .credential__star { width: 20px; height: 20px; flex: none; margin-top: -1px; fill: var(--star-red); }
</style>
</head>
<body>
<main class="flyer">
  <div class="backdrop" role="img" aria-label="Draped American flag background in red, white and navy with faint stars">
    <div class="backdrop__left"></div>
    <div class="backdrop__right"></div>
  </div>

  <div class="campaign-mark">
    <div>
      <span class="campaign-mark__name">MAREK DOLVANE</span>
      <span class="campaign-mark__line">FOR CONGRESS TEXAS-32</span>
    </div>
    <span class="campaign-mark__square"></span>
  </div>

  <svg class="headline" viewBox="0 0 613 270" aria-label="Marek, Republican for Congress">
    <text x="0" y="205" font-size="278" textLength="613" lengthAdjust="spacingAndGlyphs">MAREK</text>
    <text x="0" y="256" font-size="40" textLength="613" lengthAdjust="spacingAndGlyphs">REPUBLICAN FOR CONGRESS</text>
  </svg>

  <section class="info-box">
    <svg width="614" height="178" viewBox="0 0 614 178" style="position:absolute;left:0;top:0" aria-hidden="true">
      <polygon points="12,0 614,0 614,52 0,52 0,12" fill="var(--paper)"/>
      <polyline points="1,52 1,177 601,177 613,165 613,52" fill="none" stroke="var(--white)" stroke-width="1.5"/>
      <line x1="276.5" y1="52" x2="276.5" y2="177" stroke="var(--white)" stroke-width="1.5"/>
    </svg>
    <svg class="info-box__web" viewBox="0 0 614 52">
      <text x="21" y="39" font-size="33" font-weight="700" fill="var(--link-blue)" font-family="Josefin Sans, Arial, sans-serif" textLength="572" lengthAdjust="spacingAndGlyphs">WWW.MAREKFORCONGRESS.EXAMPLE</text>
    </svg>
    <div class="credentials">
      <ul class="credentials__col" style="list-style:none">
        <li class="credential"><svg class="credential__star" viewBox="0 0 20 20"><polygon points="10,1 12.6,7.4 19.5,7.6 14,11.9 16,18.6 10,14.7 4,18.6 6,11.9 0.5,7.6 7.4,7.4"/></svg><span>Olympic Athlete</span></li>
        <li class="credential"><svg class="credential__star" viewBox="0 0 20 20"><polygon points="10,1 12.6,7.4 19.5,7.6 14,11.9 16,18.6 10,14.7 4,18.6 6,11.9 0.5,7.6 7.4,7.4"/></svg><span>World Champion<br>Fencer</span></li>
      </ul>
      <ul class="credentials__col" style="list-style:none">
        <li class="credential"><svg class="credential__star" viewBox="0 0 20 20"><polygon points="10,1 12.6,7.4 19.5,7.6 14,11.9 16,18.6 10,14.7 4,18.6 6,11.9 0.5,7.6 7.4,7.4"/></svg><span>Army Veteran</span></li>
        <li class="credential"><svg class="credential__star" viewBox="0 0 20 20"><polygon points="10,1 12.6,7.4 19.5,7.6 14,11.9 16,18.6 10,14.7 4,18.6 6,11.9 0.5,7.6 7.4,7.4"/></svg><span>Counterintelligence<br>Officer</span></li>
      </ul>
    </div>
  </section>
</main>
</body>
</html>
```